Thistlewood Candles, Hand-poured scented soy candles

Create a logo and label design to use on my vintage country farmhouse style, all natural, hand poured soy candle jars and apothecaries. Candles will be labeled in 4 different sizes so design must be adaptable, clean, simple, telegraphic and invoke interest in the product. Think Black lettering on white or black on kraft brown. Thistlewood is the area code for New Hampshire where we make them. The labels will need a prominent area for the scent of the candle to be listed that the eyes are drawn to. Primitive country in design? Use of state attractions? Jars are a square mason style 8 ounce and 16 ounce. Tarts are a clamshell. Lids are a 70-400 series 2.5" label area. Candles are white in a clear glass jar, black lids. There will be label design sizes of 3"x 2.5" 2.5" round, 1.5"x2.5"

Target Market(s)

primitive country, farmhouse, vintage, general home decor

Contact Information for Business Card

Thistlewood Candles, all natural soy candles, hand-poured in New Hampshire, logo, phone, address. Possibly match the main label.

Logo Text

Thistlewood Candles, all natural soy candles, hand-poured in New Hampshire, area for scent description and size of container.

Font styles to use
Serif
Script

Colors

Designer to choose colors to be used in the design.

Requirements
Must have
• simple and clean, country farmhouse with a bit of vintage thrown in. possibly multiple fonts to distinguish info from scent name
Nice to have
• at this time I am open to suggestions
• Prefer scent names or brand name in an older script?
• older copperplate/Spencerian?
Should not have
• cluttered, busy, too modern, multiple colors

```html
<!DOCTYPE html>
<html lang="en">
<head>
<meta charset="utf-8">
<title>Thistlewood Candles – Jar Label</title>
<link rel="stylesheet" href="https://fonts.googleapis.com/css2?family=Rye&family=Questrial&display=swap">
<style>
  :root {
    --kraft: #c9ab7e;
    --ink: #141110;
  }
  html, body {
    margin: 0;
    padding: 0;
    width: 1200px;
    height: 1161px;
    overflow: hidden;
    background: var(--kraft);
  }
  .canvas {
    position: relative;
    width: 1200px;
    height: 1161px;
    background: var(--kraft);
  }
  .label {
    position: absolute;
    left: 0;
    top: 0;
    width: 1200px;
    height: 1161px;
  }
  .frame-outer { fill: none; stroke: var(--ink); stroke-width: 8; }
  .frame-inner { fill: none; stroke: var(--ink); stroke-width: 3; }
  .flourish { fill: var(--ink); opacity: 0.85; }
  .sprig { fill: var(--ink); opacity: 0.85; }
  .tagline {
    font-family: "Rye", serif;
    font-size: 19px;
    fill: var(--ink);
  }
  .brand-name {
    font-family: "Rye", serif;
    font-size: 84px;
    fill: var(--ink);
  }
  .rule { fill: var(--ink); }
  .brand-sub {
    font-family: "Rye", serif;
    font-size: 34px;
    fill: var(--ink);
  }
  .scent-name {
    font-family: "Questrial", sans-serif;
    font-size: 28px;
    fill: var(--ink);
  }
</style>
</head>
<body>
<div class="canvas">
  <svg class="label" viewBox="0 0 1200 1161" xmlns="http://www.w3.org/2000/svg">
    <defs>
      <path id="tagline-arc" d="M440,468 Q601,378 762,468"/>
    </defs>

    <rect class="frame-outer" x="377" y="241" width="449" height="661"/>
    <rect class="frame-inner" x="394" y="258" width="415" height="627"/>

    <rect class="flourish" x="420" y="290" width="150" height="34" rx="14" role="img" aria-label="Decorative scroll flourish, top left"/>
    <rect class="flourish" x="614" y="290" width="168" height="34" rx="14" role="img" aria-label="Decorative scroll flourish, top right"/>

    <text class="tagline">
      <textPath href="#tagline-arc" startOffset="50%" text-anchor="middle" textLength="296" lengthAdjust="spacing">ALL NATURAL SOY CANDLES</textPath>
    </text>

    <rect class="sprig" x="566" y="440" width="70" height="11" rx="5.5" role="img" aria-label="Small leaf sprig ornament"/>

    <text class="brand-name" x="601" y="580" text-anchor="middle" textLength="290" lengthAdjust="spacingAndGlyphs">Thistlewood</text>

    <rect class="rule" x="455" y="591" width="287" height="7"/>

    <text class="brand-sub" x="598" y="641" text-anchor="middle" textLength="282" lengthAdjust="spacing">CANDLES</text>

    <text class="scent-name" x="601" y="713" text-anchor="middle">scent name</text>

    <rect class="flourish" x="420" y="808" width="150" height="38" rx="14" role="img" aria-label="Decorative scroll flourish, bottom left"/>
    <rect class="flourish" x="614" y="808" width="168" height="38" rx="14" role="img" aria-label="Decorative scroll flourish, bottom right"/>
  </svg>
</div>
</body>
</html>
```